Bramleys Tea Corner Website

I need a website for a diner/restaurant that has been established in a farming, oil and industrial community for over 15 years. The website needs to be simple in design, but that should demonstrate the mastery of skills of the designer. Our diner/restaurant is family oriented, patriotic but very rustic
Fb Address is fb.me/BramleysUSA

Pictures of the restaurant

https://www.filecrate.example/s/k3vq8wz1tn0x7rb/Bramleys_05.jpg?dl=0

Pictures of About us

https://www.filecrate.example/sh/qmt604z918wle27/BBBqk7HDvtQxa2Rnhy-KP8153c?dl=0

Article about Bramley's
https://www.filecrate.example/s/7h2r61xzuvmd40p/BramleysTeaCorner1.PDF?dl=0
https://www.filecrate.example/s/w8ky37lnqjbe91c/BramleysTeaCorner2.PDF?dl=0

Project Deadline Extended
Reason: I was slow to update with information.

Project Deadline Extended
Reason: I am just getting feedback to the designs posted. I wasn't sure of the limited feedback was limiting designers from submitting designs. That and running a business with 25 employees open 12 hours a day, being here 2 hours prior and 2-3 hours after makes for long days.

I've increased the first place prize and also added funds to the second and third place prizes for your effort.

I just need the files in PSD, not HTML 5 as originally requested. We can handle getting the coding part.

Ill have the contest finalized by Monday. Thanks for your patience.

Target Market(s)

Cross section of adults from 18-35 & 35-55.

Industry/Entity Type

Industrial

Font styles to use
Other font styles liked:
• ff tisa web pro or garamond premier pro

Requirements
Must have
• Must be clean, look nice and not look like an afterthought.
Nice to have
• Please see the last two documents for information about our restaurant, which was featured in our local newspaper.

```html
<!DOCTYPE html>
<html lang="en">
<head>
<meta charset="utf-8">
<title>Bramley's Tea Corner</title>
<link rel="stylesheet" href="https://fonts.googleapis.com/css2?family=Open+Sans:wght@300;400;600;700&family=Rosarivo&display=swap">
<style>
:root{
  --red:#c40000;
  --amber:#fcab0d;
  --gold:#f9c04e;
  --maroon:#2b0d08;
  --cream:#fdedcc;
  --footer:#353535;
  --panel:#474747;
  --field:#4c4c4c;
  --ink:#222;
  --muted:#7a7a7a;
  --white:#fff;
}
*{box-sizing:border-box;margin:0;padding:0}
html,body{width:1200px;height:2470px;overflow:hidden}
body{font-family:"Open Sans",Arial,sans-serif;color:var(--ink);background:var(--footer);position:relative}
.abs{position:absolute}

/* hero */
.hero{left:0;top:0;width:1200px;height:578px;background:
  radial-gradient(ellipse 300px 260px at 300px 250px,#f3ece2 0,#d9c8b0 40%,transparent 70%),
  radial-gradient(ellipse 420px 300px at 950px 260px,#a0663a 0,transparent 70%),
  linear-gradient(135deg,#4a2c18 0%,#8a5a34 45%,#b98a55 70%,#6b4425 100%)}
.topbar{left:0;top:0;width:1200px;height:100px;background:rgba(255,255,255,.55)}
.brand{left:80px;top:30px;display:flex;align-items:center;gap:12px;font-family:"Rosarivo",Georgia,serif;font-size:30px;color:var(--red)}
.brand i{display:block;width:22px;height:22px;border-radius:50%;background:var(--red)}
.nav{top:40px;left:672px;display:flex;gap:36px;font-size:13px;letter-spacing:.5px;color:#333}
.arrow{top:308px;width:46px;height:46px;border-radius:50%;background:#a01515;display:flex;align-items:center;justify-content:center}

/* welcome */
.welcome{left:0;top:578px;width:600px;height:157px;background:var(--red);color:var(--white);text-align:center;font-size:32px;line-height:48px;padding-top:32px}
.call{left:600px;top:578px;width:600px;height:157px;background:var(--gold);color:var(--white);text-align:center;font-size:28px;padding-top:36px}
.book-btn{display:inline-block;margin-top:16px;width:300px;height:44px;line-height:44px;font-size:26px;color:#222;border-radius:22px;background:linear-gradient(90deg,rgba(255,255,255,0),#fff 20%,#fff 80%,rgba(255,255,255,0))}

/* specials */
.specials{left:0;top:735px;width:1200px;height:565px;background:linear-gradient(180deg,#2d2d30,#3b3c40 40%,#2a2a2d)}
.specials-title{left:410px;top:768px;width:450px;height:60px;line-height:60px;text-align:center;font-size:30px;color:var(--red);background:linear-gradient(90deg,#444,#fff 18%,#fff 82%,#444)}
.dish{top:873px;width:305px}
.dish h3{height:57px;line-height:57px;text-align:center;color:var(--white);font-weight:400;font-size:23px}
.dish .photo{height:205px}
.dish p{background:var(--white);font-size:11.5px;line-height:17px;padding:12px 6px 10px;height:120px;color:#222}
.dish svg{display:block}

/* testimonial */
.say{left:0;top:1300px;width:1200px;height:392px;background:var(--cream)}
.say-mark{left:100px;top:1420px;display:flex;align-items:center;gap:10px;font-family:"Rosarivo",Georgia,serif;font-size:20px;color:var(--red)}
.say-mark i{display:block;width:18px;height:18px;background:var(--red)}
.say-title{left:235px;top:1362px;width:280px;text-align:center;font-family:"Rosarivo",Georgia,serif;font-size:52px;line-height:72px;color:var(--ink)}
.say-title span{color:var(--red)}
.say-rule{left:616px;top:1335px;width:5px;height:326px;background:var(--amber)}
.quote{left:643px;top:1390px;width:455px;font-size:21.5px;line-height:29px;font-weight:300;color:#666;text-align:justify}
.quote-by{left:643px;top:1573px;font-size:19px;font-weight:700;color:#111}

.tagline{left:0;top:1692px;width:1200px;height:133px;background:var(--amber);color:var(--white);text-align:center;line-height:133px;font-family:"Rosarivo",Georgia,serif;font-size:36px}

/* footer */
.subscribe{left:80px;top:1846px;width:1038px;height:129px;background:var(--panel)}
.subscribe h4{position:absolute;left:86px;top:14px;font-weight:400;font-size:29px;color:var(--white)}
.sub-field{left:166px;top:1905px;width:694px;height:52px;background:#767676;color:#ddd;font-size:14px;line-height:52px;padding-left:14px}
.btn{background:var(--amber);color:var(--white);text-align:center;border-radius:3px}
.sub-btn{left:882px;top:1905px;width:120px;height:52px;line-height:52px;font-size:15px}
.f-head{top:2015px;font-size:26px;color:var(--white)}
.c-item{left:80px;display:flex;align-items:center;gap:26px;color:#aaa;font-size:10px;line-height:13px}
.c-item svg{flex:none}
.field{background:var(--field);color:#bbb;font-size:13px;padding:12px 12px;border-radius:3px}
.submit{left:1011px;top:2372px;width:106px;height:40px;line-height:40px;font-size:12px;font-weight:700}
.social{top:2396px;width:48px;height:48px;border-radius:50%;background:#fff;border:5px solid #ddd;box-shadow:0 2px 4px rgba(0,0,0,.5)}
.copyright{left:0;top:2432px;width:1200px;height:38px;background:#2b2b2b;color:#ccc;font-size:11px;line-height:46px;padding-left:80px}
</style>
</head>
<body>

<div class="abs hero" role="img" aria-label="Photo of a coffee cup splashing on a woven mat with coffee beans"></div>
<div class="abs topbar"></div>
<div class="abs brand"><i></i>Bramley's Tea Corner</div>
<nav class="abs nav"><span>SPECIALS</span><span>MENU</span><span>ENTERTAINMENT</span><span>ABOUT</span><span>CONTACT</span></nav>
<div class="abs arrow" style="left:12px"><svg width="14" height="16"><path d="M10 2 3 8l7 6z" fill="#fff"/></svg></div>
<div class="abs arrow" style="left:1142px"><svg width="14" height="16"><path d="M4 2l7 6-7 6z" fill="#fff"/></svg></div>

<div class="abs welcome">Welcome to<br>Bramleys Tea Corner</div>
<div class="abs call">Call us: 123456<br><span class="book-btn">Book Your table</span></div>

<section class="abs specials" role="img" aria-label="Dark rustic wood background"></section>
<div class="abs specials-title">Our Speciality</div>

<div class="abs dish" style="left:78px">
  <h3 style="background:var(--red)">Four Egg Omelets</h3>
  <div class="photo" role="img" aria-label="Photo of a folded omelet with a small flag" style="background:linear-gradient(160deg,#f2d46a,#e3a83a 55%,#c9822a)"></div>
  <p>Lorem ipsum dolor sit amet, consectetur adipiscing elit. Curabitur lacus odio, consequat iaculis sollicitudin ut, vehicula a lorem. Pellentesque odio risus, semper eget luctus gravida, iaculis porta elit.</p>
  <svg width="305" height="14"><path d="M0 0H305V6L297 14 289 6 281 14 273 6 265 14 257 6 249 14 241 6 233 14 225 6 217 14 209 6 201 14 193 6 185 14 177 6 169 14 161 6 153 14 145 6 137 14 129 6 121 14 113 6 105 14 97 6 89 14 81 6 73 14 65 6 57 14 49 6 41 14 33 6 25 14 17 6 9 14 0 6z" fill="#fff"/></svg>
</div>
<div class="abs dish" style="left:447px">
  <h3 style="background:var(--amber)">Griddle Items</h3>
  <div class="photo" role="img" aria-label="Photo of French toast with syrup and butter" style="background:radial-gradient(ellipse 120px 70px at 50% 60%,#7a3f1a,#b9733c 55%,#e9e6e0 90%)"></div>
  <p>Lorem ipsum dolor sit amet, consectetur adipiscing elit. Curabitur lacus odio, consequat iaculis sollicitudin ut, vehicula a lorem. Pellentesque odio risus, semper eget luctus gravida, iaculis porta elit.</p>
  <svg width="305" height="14"><path d="M0 0H305V10Q260 4 220 12T130 8 50 12 0 6z" fill="#fff"/></svg>
</div>
<div class="abs dish" style="left:813px">
  <h3 style="background:var(--maroon)">Cold Cuts and Salads</h3>
  <div class="photo" role="img" aria-label="Photo of a bowl of bean soup" style="background:radial-gradient(ellipse 140px 90px at 50% 50%,#c98a4a,#b06a30 60%,#e9ecef 85%)"></div>
  <p>Lorem ipsum dolor sit amet, consectetur adipiscing elit. Curabitur lacus odio, consequat iaculis sollicitudin ut, vehicula a lorem. Pellentesque odio risus, semper eget luctus gravida, iaculis porta elit.</p>
  <svg width="305" height="14"><path d="M0 0H305V8L280 12 250 4 215 12 180 6 140 13 100 5 60 12 25 6 0 12z" fill="#fff"/></svg>
</div>

<section class="abs say"></section>
<div class="abs say-mark"><i></i>Bramley's</div>
<h2 class="abs say-title" style="font-weight:400">What<br>People Are<br><span>Sayin</span></h2>
<div class="abs say-rule"></div>
<p class="abs quote">Lorem ipsum dolor sit amet, consectetur adipiscing elit. Curabitur lacus odio, consequat iaculis sollicitudin ut, vehicula a lorem. Pellentesque odio risus, semper eget luctus gravida, iaculis porta elit.</p>
<p class="abs quote-by">~ Lorem ipsum dolor sit amet</p>

<div class="abs tagline">Best Food . Entertainment . Quick Service</div>

<div class="abs subscribe"><h4>Subscribe for Updates</h4></div>
<div class="abs sub-field">Enter Your Email Address Here...</div>
<div class="abs btn sub-btn">Subscribe</div>

<h4 class="abs f-head" style="left:80px;font-weight:400">Contact Us</h4>
<div class="abs c-item" style="top:2064px"><svg width="16" height="22"><path d="M8 1a7 7 0 0 0-7 7c0 5 7 13 7 13s7-8 7-13a7 7 0 0 0-7-7z" fill="#888"/><circle cx="8" cy="8" r="2.5" fill="#353535"/></svg><span>Lorem Ipsum has been the industry's<br>standard 1500s</span></div>
<div class="abs c-item" style="top:2121px"><svg width="22" height="14"><rect x="1" y="1" width="20" height="12" fill="none" stroke="#888" stroke-width="1.5"/><path d="M1 1l10 7 10-7" fill="none" stroke="#888" stroke-width="1.5"/></svg><span>SUPPORT@BRAMLEYSMAIL.EXAMPLE</span></div>
<div class="abs c-item" style="top:2164px;font-size:20px;color:#ddd"><svg width="20" height="20"><path d="M4 2l4 4-2 3c1 2 3 4 5 5l3-2 4 4-3 3C9 18 2 11 1 5z" fill="none" stroke="#888" stroke-width="1.5"/></svg><span>0.1234565789</span></div>

<h4 class="abs f-head" style="left:416px;font-weight:400">Book Your table now</h4>
<div class="abs field" style="left:416px;top:2060px;width:699px;height:45px">Your Name</div>
<div class="abs field" style="left:416px;top:2122px;width:345px;height:45px">Your Phone</div>
<div class="abs field" style="left:772px;top:2122px;width:343px;height:45px">Your Email</div>
<div class="abs field" style="left:416px;top:2185px;width:345px;height:45px">No of people<svg style="position:absolute;right:14px;top:19px" width="10" height="6"><path d="M0 0h10L5 6z" fill="#999"/></svg></div>
<div class="abs field" style="left:772px;top:2185px;width:343px;height:45px">Preffered Date &amp; Time</div>
<div class="abs field" style="left:416px;top:2248px;width:699px;height:106px">Write your comment here...</div>
<div class="abs btn submit">SUBMIT</div>

<div class="abs copyright">Copyright © 2014 - All Rights Reserved.</div>
<div class="abs social" style="left:480px" role="img" aria-label="Social link"></div>
<div class="abs social" style="left:550px" role="img" aria-label="Social link"></div>
<div class="abs social" style="left:620px" role="img" aria-label="Social link"></div>

</body>
</html>
```